Cold pressed organic juice company is expanding to do bone broths

I need 2 labels with the same look ,different colors one for beef bone broth , one for chicken bone broth, both with the addition of medicinal mushrooms. I would like the design to clearly indicate the inclusion of the mushrooms.
the labels with be applied to compostable brown container ( paper bag brown)
Container size is 5 1/2 inches tall(14cm )
Target Market(s)
Health conscious people
Requirements
Must have
- picture of medicinal mushroom along with logo provided, either color and this phrase added to the label : A blend of Ashwagandha and 8 medicinal mushrooms
Nice to have
- maybe some illustrations of medicinal mushrooms , maybe partial black and white ?
Should not have
- no animal pictures such as chickens or cows

```html
<!DOCTYPE html>
<html lang="en">
<head>
<meta charset="utf-8">
<title>Bone Broth Labels</title>
<link rel="stylesheet" href="https://fonts.googleapis.com/css2?family=Great+Vibes&family=Josefin+Sans:wght@300;400&family=Cormorant+Garamond:ital,wght@1,400;1,500&display=swap">
<style>
  :root {
    --backdrop: #f2dccb;
    --paper: #ffffff;
    --beef: #7d0000;
    --chicken: #d35400;
    --frame-line: #5a2a14;
    --accent-text: #8b3a10;
    --ink: #111111;
    --shroom-peach: #f6c9a8;
    --shroom-orange: #f39a5a;
    --shroom-rust: #b8500f;
    --shroom-taupe: #8a7a6c;
    --shroom-lilac: #d8d0d4;
    --icon-line: #9a6a5a;
  }
  * { margin: 0; padding: 0; box-sizing: border-box; }
  html, body { width: 1200px; height: 1000px; overflow: hidden; }
  body { background: var(--backdrop); position: relative; }

  .label {
    position: absolute;
    width: 413px;
    height: 496px;
    background: var(--paper);
    --brand: var(--beef);
  }
  .label--beef { left: 134px; top: 221px; --brand: var(--beef); }
  .label--chicken { left: 637px; top: 218px; --brand: var(--chicken); }

  .label__frame {
    position: absolute;
    left: 76px; top: 62px;
    width: 257px; height: 372px;
    border: 1px solid var(--frame-line);
  }
  .label__band {
    position: absolute;
    left: -1px; right: 0; top: 228px; height: 48px;
    background: var(--brand);
    display: flex; align-items: center; justify-content: center;
  }
  .label__band-text {
    font-family: "Josefin Sans", sans-serif;
    font-weight: 300;
    font-size: 26px;
    letter-spacing: 3px;
    color: #fff;
    padding-top: 5px;
    margin-left: 3px;
  }
  .label__brand {
    position: absolute;
    left: 164px; top: 0;
    width: 85px; height: 85px;
    background: var(--brand);
    display: flex; align-items: center; justify-content: center;
  }
  .brand-mark {
    width: 64px; height: 64px;
    border: 1.5px solid #fff;
    border-radius: 50%;
    display: flex; align-items: center; justify-content: center;
    text-align: center;
    font-family: "Cormorant Garamond", serif;
    font-style: italic;
    font-weight: 500;
    font-size: 13px;
    line-height: 1.05;
    color: #fff;
  }
  .label__flavour {
    position: absolute;
    left: 76px; width: 257px; top: 145px;
    text-align: center;
    font-family: "Great Vibes", cursive;
    font-size: 64px;
    line-height: 1;
    color: var(--ink);
  }
  .label__icon { position: absolute; left: 189px; top: 285px; width: 34px; height: 34px; }
  .label__tagline {
    position: absolute;
    left: 60px; width: 290px; top: 350px;
    text-align: center;
    font-family: "Cormorant Garamond", serif;
    font-style: italic;
    font-size: 21px;
    line-height: 26px;
    color: var(--ink);
  }
  .label__tagline em { font-style: italic; color: var(--accent-text); }
  .label__foot {
    position: absolute;
    left: 77px; top: 482px;
    width: 257px; height: 14px;
    background: var(--brand);
  }
  .mushroom {
    position: absolute;
    border-radius: 45% 45% 30% 30%;
  }
  .mushroom--a { left: 17px; top: 34px; width: 51px; height: 50px; background: linear-gradient(var(--shroom-rust) 25%, var(--shroom-peach) 25%); }
  .mushroom--b { left: 28px; top: 136px; width: 23px; height: 76px; background: linear-gradient(var(--shroom-taupe) 45%, var(--shroom-lilac) 45%); }
  .mushroom--c { left: 18px; top: 316px; width: 44px; height: 50px; background: linear-gradient(var(--shroom-orange) 35%, var(--shroom-peach) 35%); }
  .mushroom--d { left: 10px; top: 428px; width: 52px; height: 46px; background: linear-gradient(#3a2a22 15%, var(--shroom-peach) 15%); }
  .mushroom--e { left: 341px; top: 28px; width: 49px; height: 62px; background: var(--shroom-peach); }
  .mushroom--f { left: 349px; top: 153px; width: 42px; height: 38px; background: linear-gradient(135deg, var(--shroom-rust), var(--shroom-peach)); border-radius: 50%; }
  .mushroom--g { left: 341px; top: 311px; width: 47px; height: 38px; background: linear-gradient(#3a2f2a, var(--shroom-lilac)); }
  .mushroom--h { left: 355px; top: 404px; width: 35px; height: 71px; background: linear-gradient(var(--shroom-lilac), #ece6e8); }
</style>
</head>
<body>

<section class="label label--beef">
  <div class="mushroom mushroom--a" role="img" aria-label="Illustration of a rust-capped medicinal mushroom"></div>
  <div class="mushroom mushroom--b" role="img" aria-label="Illustration of a tall grey-capped mushroom"></div>
  <div class="mushroom mushroom--c" role="img" aria-label="Illustration of an orange-capped mushroom"></div>
  <div class="mushroom mushroom--d" role="img" aria-label="Illustration of a flat-capped gilled mushroom"></div>
  <div class="mushroom mushroom--e" role="img" aria-label="Illustration of a chanterelle mushroom"></div>
  <div class="mushroom mushroom--f" role="img" aria-label="Illustration of a round orange mushroom"></div>
  <div class="mushroom mushroom--g" role="img" aria-label="Illustration of turkey tail mushroom"></div>
  <div class="mushroom mushroom--h" role="img" aria-label="Illustration of a cluster of small pale mushrooms"></div>

  <div class="label__frame"></div>
  <div class="label__band"><span class="label__band-text">BONE BROTH</span></div>
  <div class="label__brand"><div class="brand-mark">Solstice<br>Press</div></div>
  <div class="label__flavour">Beef</div>
  <svg class="label__icon" viewBox="0 0 34 34" aria-hidden="true">
    <g fill="none" stroke="var(--icon-line)" stroke-width="1">
      <line x1="10" y1="24" x2="24" y2="10"/>
      <circle cx="24" cy="6" r="3"/><circle cx="28" cy="10" r="3"/>
      <circle cx="6" cy="24" r="3"/><circle cx="10" cy="28" r="3"/>
    </g>
  </svg>
  <p class="label__tagline"><em>A blend of</em> Ashwagandha<br><em>and</em> 8 medicinal <em>mushrooms</em></p>
  <div class="label__foot"></div>
</section>

<section class="label label--chicken">
  <div class="mushroom mushroom--a" role="img" aria-label="Illustration of a rust-capped medicinal mushroom"></div>
  <div class="mushroom mushroom--b" role="img" aria-label="Illustration of a tall grey-capped mushroom"></div>
  <div class="mushroom mushroom--c" role="img" aria-label="Illustration of an orange-capped mushroom"></div>
  <div class="mushroom mushroom--d" role="img" aria-label="Illustration of a flat-capped gilled mushroom"></div>
  <div class="mushroom mushroom--e" role="img" aria-label="Illustration of a chanterelle mushroom"></div>
  <div class="mushroom mushroom--f" role="img" aria-label="Illustration of a round orange mushroom"></div>
  <div class="mushroom mushroom--g" role="img" aria-label="Illustration of turkey tail mushroom"></div>
  <div class="mushroom mushroom--h" role="img" aria-label="Illustration of a cluster of small pale mushrooms"></div>

  <div class="label__frame"></div>
  <div class="label__band"><span class="label__band-text">BONE BROTH</span></div>
  <div class="label__brand"><div class="brand-mark">Solstice<br>Press</div></div>
  <div class="label__flavour">Chicken</div>
  <svg class="label__icon" viewBox="0 0 34 34" aria-hidden="true">
    <path d="M17 3 C 12 10, 8 18, 9 30 M17 3 C 20 10, 24 18, 23 32" fill="none" stroke="#333" stroke-width="1"/>
  </svg>
  <p class="label__tagline"><em>A blend of</em> Ashwagandha<br><em>and</em> 8 medicinal <em>mushrooms</em></p>
  <div class="label__foot"></div>
</section>

</body>
</html>
```